Velmin & Co Powerpoint Template

A simple powerpoint template for my business which provides management consulting services for Business Owners.

It should reflect the colours within the logo design and should work as the master template for all standard powerpoint slide layouts.

```html
<!DOCTYPE html>
<html lang="en">
<head>
<meta charset="utf-8">
<title>Velmin &amp; Co — Presentation Template</title>
<link rel="stylesheet" href="https://fonts.googleapis.com/css2?family=Poppins:wght@400;600;700&display=swap">
<style>
:root{
  --orange:#e35a1e;
  --ink:#1f2022;
  --text:#4d4d4d;
  --muted:#6b6b6b;
  --mint:#eef6f4;
  --white:#ffffff;
  --grey-bar:#4a4a4a;
  --black-bar:#111111;
  --board:#c6c6c6;
}
*{box-sizing:border-box;margin:0;padding:0}
html,body{width:1200px;height:2435px;overflow:hidden}
body{background:var(--board);font-family:'Poppins',sans-serif;position:relative;color:var(--ink)}

.hero{position:absolute;left:0;top:0;width:1200px;height:705px;background:linear-gradient(180deg,#e6e8ee 0%,#d3d6dc 100%)}
.hero-slide{transform:scale(1.28);transform-origin:0 0;left:110px!important;top:160px!important}
.hero-brand{position:absolute;left:960px;top:95px;font-size:22px;color:#222}

.slide{position:absolute;width:563px;height:316px;overflow:hidden;background:var(--white)}
.slide.dark{background:#151617;color:var(--white)}
.photo{position:absolute}
.photo-dark{inset:0;background:radial-gradient(ellipse at 65% 40%,#3a3e43 0%,#222427 45%,#121314 100%)}
.photo-city{inset:0;background:linear-gradient(160deg,#3b3f44 0%,#1c1e21 55%,#0f1011 100%)}

.brand{position:absolute;display:flex;align-items:center;gap:8px;font-size:15px;font-weight:400;white-space:nowrap}
.brand-dot{width:14px;height:14px;border-radius:50%;background:var(--orange);flex:none}

.title-block{position:absolute}
.title{font-size:25px;line-height:1.15;color:var(--orange);font-weight:400}
.title b{font-weight:700}
.subtitle{font-size:12px;margin-top:4px;font-weight:400}
.date{font-size:6.5px;margin-top:14px;letter-spacing:2px;font-weight:600}
.date.tight{letter-spacing:0}
.panel{position:absolute;background:var(--mint);color:var(--ink)}
.accent-bar{position:absolute;height:8px;background:var(--orange)}

.band{position:absolute;left:0;right:0;bottom:0;height:23px;background:var(--mint);color:var(--ink);font-size:5.5px;display:flex;align-items:center;justify-content:center}
.band b{font-weight:600}

.heading{position:absolute;font-size:14px;font-weight:400;color:#3a3a3a}
.heading b{font-weight:600}
.heading::after{content:"";display:block;width:30px;height:3px;background:var(--orange);margin-top:7px}
.heading.center{text-align:center}
.heading.center::after{margin:6px auto 0}
.sub-heading{font-size:10px;color:var(--orange);font-weight:400;margin-bottom:7px}
.sub-heading b{font-weight:600}
.copy{font-size:7px;line-height:1.12;color:var(--text)}
.copy p{margin-bottom:6px}
.bullets{list-style:none;font-size:6.5px;line-height:1.12;color:var(--text)}
.bullets li{position:relative;padding-left:13px;margin-bottom:6px}
.bullets li::before{content:"";position:absolute;left:1px;top:2px;width:3px;height:3px;border-radius:50%;background:var(--orange)}
.col{position:absolute;width:230px}

.foot-brand{left:16px;bottom:16px;font-size:9px;color:#333;gap:6px}
.foot-brand .brand-dot{width:10px;height:10px}
.folio{position:absolute;right:16px;bottom:17px;display:flex;align-items:center;gap:8px;font-size:5.5px;color:#333}
.folio b{font-weight:600}
.page{width:10px;height:10px;background:var(--orange);color:#fff;font-size:5px;display:flex;align-items:center;justify-content:center;border-radius:1px}

.donut{position:absolute;text-align:center;width:120px}
.donut .val{position:absolute;left:0;right:0;top:43px;font-size:24px;font-weight:400}
.donut p{font-size:6px;line-height:1.1;color:var(--muted);margin-top:10px}

.legend{position:absolute;left:313px;width:210px}
.legend-item{display:flex;align-items:center;gap:6px;margin-bottom:16px}
.legend-key{width:9px;height:9px;flex:none}
.legend-box{border:1px solid #d9d9d9;border-radius:5px;padding:6px 16px;font-size:6px;line-height:1.12;color:var(--text)}

.contact{position:absolute;left:48px;top:163px;color:#fff}
.contact h2{font-size:11px;font-weight:600;margin-bottom:10px}
.contact li{list-style:none;display:flex;align-items:center;gap:8px;font-size:7.5px;margin-bottom:6px}
</style>
</head>
<body>

<section class="hero">
  <div class="slide dark hero-slide">
    <div class="photo photo-dark" role="img" aria-label="Dark photograph of a business handshake above a laptop"></div>
    <div class="brand" style="left:52px;top:70px;color:#fff"><span class="brand-dot"></span><span>Velmin &amp; Co</span></div>
    <div class="title-block" style="left:52px;top:170px">
      <h1 class="title"><b>Presentation Title</b><br>Goes Here</h1>
      <p class="subtitle">Subtitle of Presentation Goes Here</p>
      <p class="date">Friday, September 1, 2023</p>
    </div>
    <div class="band"><span><b>© Velmin &amp; Co</b> 2023. All Rights Reserved.</span></div>
  </div>
  <div class="brand hero-brand"><span class="brand-dot" style="width:20px;height:20px"></span><span>Velmin &amp; Co</span></div>
</section>

<div class="slide dark" style="left:28px;top:746px">
  <div class="photo photo-dark" role="img" aria-label="Dark photograph of a business handshake above a laptop"></div>
  <div class="brand" style="left:52px;top:70px;color:#fff"><span class="brand-dot"></span><span>Velmin &amp; Co</span></div>
  <div class="title-block" style="left:52px;top:170px">
    <h1 class="title"><b>Presentation Title</b><br>Goes Here</h1>
    <p class="subtitle">Subtitle of Presentation Goes Here</p>
    <p class="date">Friday, September 1, 2023</p>
  </div>
  <div class="band"><span><b>© Velmin &amp; Co</b> 2023. All Rights Reserved.</span></div>
</div>

<div class="slide dark" style="left:609px;top:746px">
  <div class="photo photo-dark" role="img" aria-label="Dark photograph of a business handshake above a laptop"></div>
  <div class="panel" style="left:0;top:92px;width:362px;height:131px"></div>
  <div class="title-block" style="left:51px;top:104px;color:var(--ink)">
    <h1 class="title"><b>Presentation Title<br>Goes Here</b></h1>
    <p class="subtitle">Subtitle of Presentation Goes Here</p>
    <p class="date tight">Friday, September 1, 2023</p>
  </div>
  <div class="accent-bar" style="left:51px;top:220px;width:250px"></div>
  <div class="brand" style="left:400px;top:150px;color:#fff"><span class="brand-dot"></span><span>Velmin &amp; Co</span></div>
</div>

<div class="slide dark" style="left:28px;top:1081px">
  <div class="photo photo-dark" role="img" aria-label="Dark photograph of a business handshake above a laptop"></div>
  <div class="brand" style="left:52px;top:50px;color:#fff"><span class="brand-dot"></span><span>Velmin &amp; Co</span></div>
  <div class="panel" style="left:0;top:120px;width:414px;height:131px"></div>
  <div class="title-block" style="left:51px;top:131px;color:var(--ink)">
    <h1 class="title"><b>Presentation Title<br>Goes Here</b></h1>
    <p class="subtitle">Subtitle of Presentation Goes Here</p>
    <p class="date tight">Friday, September 1, 2023</p>
  </div>
  <div class="accent-bar" style="left:52px;top:247px;width:249px"></div>
</div>

<div class="slide" style="left:609px;top:1081px">
  <h2 class="heading" style="left:36px;top:34px"><b>Heading</b> Goes Here</h2>
  <div class="copy" style="position:absolute;left:36px;top:80px;width:235px">
    <p>Duis eget tellus porta, consequat lacus vitae, venenatis dolor. Nulla facilisi. In et sollicitudin lacus. Donec risus orci, gravida sit amet risus vehicula, aliquet pretium sapien. Nullam sit amet magna non ex bibendum mollis. Nunc vel neque eu augue dignissim congue ut vitae magna. Phasellus eget commodo arcu.</p>
    <ul class="bullets">
      <li>Lorem ipsum dolor sit amet, consectetur adipiscing elit. Vivamus eu dui ex. Curabitur dapibus dignissim dui, in molestie metus feugiat sed.</li>
      <li>Duis eget tellus porta, consequat lacus vitae, venenatis dolor.</li>
      <li>Nulla facilisi. In et sollicitudin lacus. Donec risus orci, gravida sit amet risus vehicula, aliquet pretium sapien.</li>
      <li>Duis eget tellus porta, consequat lacus vitae, venenatis dolor. Nulla facilisi.</li>
      <li>In et sollicitudin lacus. Donec risus orci, gravida sit amet risus vehicula, aliquet pretium sapien.</li>
    </ul>
  </div>
  <div class="photo" style="left:300px;top:0;width:225px;height:264px;background:linear-gradient(160deg,#d8d2c8,#eef0f3 55%,#b9b2aa)" role="img" aria-label="Photograph of hands reviewing and signing a document"></div>
  <div class="brand foot-brand"><span class="brand-dot"></span><span>Velmin &amp; Co</span></div>
  <div class="folio"><span><b>© Velmin &amp; Co</b> 2023. All Rights Reserved.</span><span class="page">4</span></div>
</div>

<div class="slide" style="left:28px;top:1416px">
  <h2 class="heading" style="left:36px;top:20px"><b>Heading</b> Goes Here</h2>
  <div class="col" style="left:36px;top:73px">
    <h3 class="sub-heading"><b>Heading</b> Goes Here</h3>
    <div class="copy">
      <p>Lorem ipsum dolor sit amet, consectetur adipiscing elit. Vivamus eu dui ex. Curabitur dapibus dignissim dui, in molestie metus feugiat sed. Praesent aliquet lorem ex, eu dapibus odio varius at.</p>
      <p>Duis eget tellus porta, consequat lacus vitae, venenatis dolor. Nulla facilisi. In et sollicitudin lacus. Donec risus orci, gravida sit amet risus vehicula, aliquet pretium sapien. Nullam sit amet magna non ex bibendum mollis. Nunc vel neque eu augue dignissim congue ut vitae magna. Phasellus eget commodo arcu.</p>
      <p>Nunc vitae semper dui. Integer venenatis, tellus sit amet interdum pretium, erat neque rhoncus turpis, a aliquam augue ligula eget erat.</p>
      <p>Nunc placerat, arcu nec mattis fermentum, nisi mauris convallis nunc, ut luctus nunc nisl id ex.</p>
    </div>
  </div>
  <div class="col" style="left:296px;top:73px">
    <h3 class="sub-heading"><b>Heading</b> Goes Here</h3>
    <div class="copy">
      <p>Lorem ipsum dolor sit amet, consectetur adipiscing elit. Vivamus eu dui ex. Curabitur dapibus dignissim dui, in molestie metus feugiat sed. Praesent aliquet lorem ex, eu dapibus odio varius at.</p>
      <p>Duis eget tellus porta, consequat lacus vitae, venenatis dolor. Nulla facilisi. In et sollicitudin lacus. Donec risus orci, gravida sit amet risus vehicula, aliquet pretium sapien. Nullam sit amet magna non ex bibendum mollis. Nunc vel neque eu augue dignissim congue ut vitae magna. Phasellus eget commodo arcu.</p>
      <p>Nunc vitae semper dui. Integer venenatis, tellus sit amet interdum pretium, erat neque rhoncus turpis, a aliquam augue ligula eget erat.</p>
      <p>Nunc placerat, arcu nec mattis fermentum, nisi mauris convallis nunc, ut luctus nunc nisl id ex.</p>
    </div>
  </div>
  <div class="brand foot-brand"><span class="brand-dot"></span><span>Velmin &amp; Co</span></div>
  <div class="folio"><span><b>© Velmin &amp; Co</b> 2023. All Rights Reserved.</span><span class="page">5</span></div>
</div>

<div class="slide" style="left:609px;top:1416px">
  <div class="photo" style="left:0;top:0;width:563px;height:146px;background:linear-gradient(100deg,#e9edf1,#f4f5f7 50%,#dfe3e8)" role="img" aria-label="Photograph of a pen over printed bar and line charts"></div>
  <h2 class="heading center" style="left:0;right:0;top:162px"><b>Heading</b> Goes Here</h2>
  <p class="copy" style="position:absolute;left:33px;right:33px;top:200px;text-align:center;font-size:6.5px">Lorem ipsum dolor sit amet, consectetur adipiscing elit. Vivamus eu dui ex. Curabitur dapibus dignissim dui, in molestie metus feugiat sed. Praesent aliquet lorem ex, eu dapibus odio varius at. Duis eget tellus porta, consequat lacus vitae, venenatis dolor. Nulla facilisi. In et sollicitudin lacus. Donec risus orci, gravida sit amet risus vehicula, aliquet pretium sapien. Nullam sit amet magna non ex bibendum mollis. Nunc vel neque eu augue dignissim congue ut vitae magna. Phasellus eget commodo arcu. Nunc vitae semper dui. Integer venenatis, tellus sit amet interdum pretium, erat neque rhoncus turpis, a aliquam augue ligula eget erat. Nunc placerat, arcu nec mattis fermentum, nisi mauris convallis nunc, ut luctus nunc nisl id ex. Nam semper tristique mauris, et vestibulum leo fringilla vel.</p>
  <div class="brand foot-brand"><span class="brand-dot"></span><span>Velmin &amp; Co</span></div>
  <div class="folio"><span><b>© Velmin &amp; Co</b> 2023. All Rights Reserved.</span><span class="page">6</span></div>
</div>

<div class="slide" style="left:28px;top:1750px">
  <h2 class="heading" style="left:36px;top:20px"><b>Heading</b> Goes Here</h2>
  <div class="col" style="left:36px;top:73px">
    <h3 class="sub-heading"><b>Heading</b> Goes Here</h3>
    <ul class="bullets" style="font-size:7px">
      <li>Lorem ipsum dolor sit amet, consectetur adipiscing elit. Vivamus eu dui ex. Curabitur dapibus dignissim dui, in molestie metus feugiat sed.</li>
      <li>Duis eget tellus porta, consequat lacus vitae, venenatis dolor.</li>
      <li>Nulla facilisi. In et sollicitudin lacus. Donec risus orci, gravida sit amet risus vehicula, aliquet pretium sapien.</li>
      <li>Nullam sit amet magna non ex bibendum mollis. Nunc vel neque eu augue dignissim congue ut vitae magna. Phasellus eget commodo arcu.</li>
      <li>Nunc vitae semper dui. Integer venenatis, tellus sit amet interdum pretium, erat neque rhoncus turpis, a aliquam augue ligula eget erat.</li>
    </ul>
  </div>
  <div class="col" style="left:296px;top:73px">
    <h3 class="sub-heading"><b>Heading</b> Goes Here</h3>
    <ul class="bullets" style="font-size:7px">
      <li>Lorem ipsum dolor sit amet, consectetur adipiscing elit. Vivamus eu dui ex. Curabitur dapibus dignissim dui, in molestie metus feugiat sed.</li>
      <li>Duis eget tellus porta, consequat lacus vitae, venenatis dolor.</li>
      <li>Nulla facilisi. In et sollicitudin lacus. Donec risus orci, gravida sit amet risus vehicula, aliquet pretium sapien.</li>
      <li>Nullam sit amet magna non ex bibendum mollis. Nunc vel neque eu augue dignissim congue ut vitae magna. Phasellus eget commodo arcu.</li>
      <li>Nunc vitae semper dui. Integer venenatis, tellus sit amet interdum pretium, erat neque rhoncus turpis, a aliquam augue ligula eget erat.</li>
    </ul>
  </div>
  <div class="brand foot-brand"><span class="brand-dot"></span><span>Velmin &amp; Co</span></div>
  <div class="folio"><span><b>© Velmin &amp; Co</b> 2023. All Rights Reserved.</span><span class="page">7</span></div>
</div>

<div class="slide" style="left:609px;top:1750px">
  <h2 class="heading" style="left:36px;top:20px"><b>Heading</b> Goes Here</h2>
  <div class="copy" style="position:absolute;left:36px;top:70px;width:190px;font-size:7px">
    <p>Lorem ipsum dolor sit amet, consectetur adipiscing elit. Vivamus eu dui ex. Curabitur dapibus dignissim dui, in molestie metus feugiat sed. Praesent aliquet lorem ex, eu dapibus odio varius at. Duis eget tellus porta, consequat lacus vitae, venenatis dolor. Nulla facilisi. In et sollicitudin lacus.</p>
    <p>Donec risus orci, gravida sit amet risus vehicula, aliquet pretium sapien. Nullam sit amet magna non ex bibendum mollis. Nunc vel neque eu augue dignissim congue ut vitae magna. Phasellus eget commodo arcu. Nunc vitae semper dui. Integer venenatis, tellus sit amet interdum pretium, erat neque rhoncus turpis, a aliquam augue ligula eget erat. Nunc placerat, arcu nec mattis fermentum, nisi mauris convallis nunc, ut luctus nunc nisl id ex.</p>
  </div>
  <div class="donut" style="left:248px;top:82px">
    <svg width="120" height="120" viewBox="0 0 120 120"><circle cx="60" cy="60" r="54" fill="none" stroke="var(--orange)" stroke-width="7" stroke-dasharray="217.1 339.3" transform="rotate(-90 60 60)"/></svg>
    <span class="val" style="color:var(--orange)">64%</span>
    <p>Lorem ipsum dolor sit amet,<br>consectetur adipiscing elit.<br>Vivamus eu dui ex. Curabitur<br>dapibus dignissim.</p>
  </div>
  <div class="donut" style="left:384px;top:82px">
    <svg width="120" height="120" viewBox="0 0 120 120"><circle cx="60" cy="60" r="54" fill="none" stroke="var(--grey-bar)" stroke-width="7" stroke-dasharray="278.2 339.3" transform="rotate(-90 60 60)"/></svg>
    <span class="val" style="color:var(--grey-bar)">82%</span>
    <p>Lorem ipsum dolor sit amet,<br>consectetur adipiscing elit.<br>Vivamus eu dui ex. Curabitur<br>dapibus dignissim.</p>
  </div>
  <div class="brand foot-brand"><span class="brand-dot"></span><span>Velmin &amp; Co</span></div>
  <div class="folio"><span><b>© Velmin &amp; Co</b> 2023. All Rights Reserved.</span><span class="page">8</span></div>
</div>

<div class="slide" style="left:28px;top:2086px">
  <h2 class="heading" style="left:36px;top:20px"><b>Heading</b> Goes Here</h2>
  <svg class="chart" style="position:absolute;left:0;top:0" width="300" height="260" viewBox="0 0 300 260" font-family="Poppins, sans-serif" font-size="5" fill="#555">
    <g stroke="#e2e2e2" stroke-width="0.6">
      <line x1="50" y1="90" x2="290" y2="90"/><line x1="50" y1="115" x2="290" y2="115"/><line x1="50" y1="140" x2="290" y2="140"/><line x1="50" y1="165" x2="290" y2="165"/><line x1="50" y1="190" x2="290" y2="190"/><line x1="50" y1="215" x2="290" y2="215"/><line x1="50" y1="240" x2="290" y2="240" stroke="#bbb"/>
    </g>
    <g text-anchor="end"><text x="46" y="92">6</text><text x="46" y="117">5</text><text x="46" y="142">4</text><text x="46" y="167">3</text><text x="46" y="192">2</text><text x="46" y="217">1</text><text x="46" y="242">0</text></g>
    <g fill="var(--orange)"><rect x="67" y="132.5" width="9" height="107.5"/><rect x="128" y="177.5" width="9" height="62.5"/><rect x="189" y="152.5" width="9" height="87.5"/><rect x="250" y="127.5" width="9" height="112.5"/></g>
    <g fill="var(--grey-bar)"><rect x="77" y="180" width="9" height="60"/><rect x="138" y="130" width="9" height="110"/><rect x="199" y="195" width="9" height="45"/><rect x="260" y="170" width="9" height="70"/></g>
    <g fill="var(--black-bar)"><rect x="87" y="190" width="9" height="50"/><rect x="148" y="190" width="9" height="50"/><rect x="209" y="165" width="9" height="75"/><rect x="270" y="115" width="9" height="125"/></g>
    <g text-anchor="middle" font-size="4.5">
      <text x="71.5" y="130">4.3</text><text x="81.5" y="177">2.4</text><text x="91.5" y="187">2</text>
      <text x="132.5" y="175">2.5</text><text x="142.5" y="127">4.4</text><text x="152.5" y="187">2</text>
      <text x="193.5" y="150">3.5</text><text x="203.5" y="192">1.8</text><text x="213.5" y="162">3</text>
      <text x="254.5" y="125">4.5</text><text x="264.5" y="167">2.8</text><text x="274.5" y="112">5</text>
    </g>
    <g text-anchor="middle" font-size="4.5"><text x="81.5" y="250">Category 1</text><text x="142.5" y="250">Category 2</text><text x="203.5" y="250">Category 3</text><text x="264.5" y="250">Category 4</text></g>
  </svg>
  <div class="legend" style="top:83px">
    <div class="legend-item"><span class="legend-key" style="background:var(--orange)"></span><p class="legend-box">Lorem ipsum dolor sit amet, consectetur adipiscing elit. Vivamus eu dui ex. Curabitur dapibus dignissim dui, in molestie metus.</p></div>
    <div class="legend-item"><span class="legend-key" style="background:var(--grey-bar)"></span><p class="legend-box">Lorem ipsum dolor sit amet, consectetur adipiscing elit. Vivamus eu dui ex. Curabitur dapibus dignissim dui, in molestie metus.</p></div>
    <div class="legend-item"><span class="legend-key" style="background:var(--black-bar)"></span><p class="legend-box">Lorem ipsum dolor sit amet, consectetur adipiscing elit. Vivamus eu dui ex. Curabitur dapibus dignissim dui, in molestie metus.</p></div>
  </div>
  <div class="brand foot-brand"><span class="brand-dot"></span><span>Velmin &amp; Co</span></div>
  <div class="folio"><span><b>© Velmin &amp; Co</b> 2023. All Rights Reserved.</span><span class="page">9</span></div>
</div>

<div class="slide dark" style="left:609px;top:2086px">
  <div class="photo photo-city" role="img" aria-label="Dark photograph looking up at glass office towers"></div>
  <div class="brand" style="left:52px;top:75px;color:#fff"><span class="brand-dot"></span><span>Velmin &amp; Co</span></div>
  <div class="contact">
    <h2>Contact Us</h2>
    <ul>
      <li><svg width="10" height="10" viewBox="0 0 24 24"><path d="M6.6 10.8a15 15 0 0 0 6.6 6.6l2.2-2.2a1 1 0 0 1 1-.25 11.4 11.4 0 0 0 3.6.57 1 1 0 0 1 1 1V20a1 1 0 0 1-1 1A17 17 0 0 1 3 4a1 1 0 0 1 1-1h3.5a1 1 0 0 1 1 1c0 1.25.2 2.45.57 3.57a1 1 0 0 1-.25 1z" fill="var(--orange)"/></svg>Phone Number Goes Here</li>
      <li><span style="color:var(--orange);font-size:10px;font-weight:600;width:10px;line-height:1">@</span>E-Mail Address Goes Here</li>
      <li><svg width="10" height="10" viewBox="0 0 24 24" fill="none" stroke="var(--orange)" stroke-width="2"><circle cx="12" cy="12" r="10"/><ellipse cx="12" cy="12" rx="4.5" ry="10"/><line x1="2" y1="12" x2="22" y2="12"/></svg>URL Address Goes Here</li>
    </ul>
  </div>
  <div class="band"><span><b>© Velmin &amp; Co</b> 2023. All Rights Reserved.</span></div>
</div>

</body>
</html>
```